LABEL DESIGN FOR A BEEF SALAMI BRAND

The BRANVOLD STORE FACTORY is located in Montreal (Canada) and we are specialized in the dried salami industry. For this project, we have to design a line of 4 flavors of BAKED BEEF SALAMI. We are looking for labels that will help us improve our products. natural / handcrafted style to our product.

Target Market(s)

LOVERS OF SALAMI AND FLESH

Industry/Entity Type

Meatpacking

Font styles to use
Script

Colors

Designer to choose colors to be used in the design.

Requirements
Should not have
• any pork congestion

```html
<!DOCTYPE html>
<html lang="en">
<head>
<meta charset="utf-8">
<title>Chorizo Beef Dried Salami – Label</title>
<link href="https://fonts.googleapis.com/css2?family=Graduate&family=Yellowtail&family=Libre+Baskerville&display=swap" rel="stylesheet">
<style>
  :root {
    --backdrop: #e4e2de;
    --cream: #efe7d4;
    --cream-light: #f6f0e2;
    --wine: #9b2a24;
    --wine-bright: #c0352c;
    --ink: #1f1d1c;
    --white: #ffffff;
  }
  html, body {
    margin: 0;
    width: 1200px;
    height: 1200px;
    overflow: hidden;
    background: var(--backdrop);
  }
  .canvas {
    position: relative;
    width: 1200px;
    height: 1200px;
  }
  .product-label {
    position: absolute;
    left: 300px;
    top: 70px;
    width: 600px;
    height: 1029px;
  }
  .slab { font-family: "Graduate", serif; }
  .script { font-family: "Yellowtail", cursive; }
  .brand { font-family: "Libre Baskerville", serif; }
</style>
</head>
<body>
<main class="canvas">
  <svg class="product-label" viewBox="0 0 490 840" xmlns="http://www.w3.org/2000/svg">
    <!-- cream label body -->
    <path class="label-body" fill="var(--cream)"
      d="M40 0 H450 A40 40 0 0 0 490 40 V700 A40 40 0 0 0 450 740 H40 A40 40 0 0 0 0 700 V40 A40 40 0 0 0 40 0 Z"/>
    <!-- inner frame -->
    <path class="label-frame" fill="none" stroke="var(--wine)" stroke-width="3"
      d="M52 14 H438 A40 40 0 0 0 476 52 V688 A40 40 0 0 0 438 726 H52 A40 40 0 0 0 14 688 V52 A40 40 0 0 0 52 14 Z"/>
    <path fill="none" stroke="var(--wine)" stroke-width="1"
      d="M56 20 H434 A38 38 0 0 0 470 56 V684 A38 38 0 0 0 434 720 H56 A38 38 0 0 0 20 684 V56 A38 38 0 0 0 56 20 Z"/>

    <!-- title band -->
    <rect class="title-band" x="22" y="150" width="446" height="222" fill="var(--ink)"/>
    <g class="slab" text-anchor="middle">
      <text x="248" y="268" font-size="66" fill="var(--wine)">CHORIZO</text>
      <text x="245" y="265" font-size="66" fill="var(--white)">CHORIZO</text>
      <text x="247" y="308" font-size="34" fill="var(--wine)">BEEF</text>
      <text x="245" y="306" font-size="34" fill="var(--white)">BEEF</text>
      <text x="247" y="348" font-size="34" fill="var(--wine)">DRIED SALAMI</text>
      <text x="245" y="346" font-size="34" fill="var(--white)">DRIED SALAMI</text>
    </g>

    <!-- tagline -->
    <rect x="22" y="452" width="446" height="22" fill="var(--ink)"/>
    <ellipse cx="245" cy="463" rx="152" ry="44" fill="var(--wine)" stroke="var(--cream-light)" stroke-width="2"/>
    <text class="script" x="245" y="454" font-size="32" fill="var(--cream-light)" text-anchor="middle">Dried To</text>
    <text class="script" x="245" y="488" font-size="32" fill="var(--cream-light)" text-anchor="middle">Perfection</text>

    <!-- claims -->
    <text class="slab" x="245" y="561" font-size="18" fill="var(--ink)" text-anchor="middle">GLUTEN / LACTOSE / ALLERGY FREE</text>

    <!-- inspection badge -->
    <circle cx="86" cy="650" r="38" fill="none" stroke="var(--ink)" stroke-width="2"/>
    <circle cx="86" cy="650" r="31" fill="none" stroke="var(--ink)" stroke-width="1"/>

    <text class="slab" x="155" y="667" font-size="14" fill="var(--ink)">KEEP REFRIGERATED</text>
    <text class="slab" x="128" y="700" font-size="14" fill="var(--ink)">NET WEIGHT : 80G ( 2.82 OZ )</text>

    <!-- brand seal -->
    <ellipse cx="245" cy="775" rx="158" ry="64" fill="var(--cream)"/>
    <ellipse cx="245" cy="775" rx="150" ry="57" fill="var(--ink)" stroke="var(--wine)" stroke-width="4"/>
    <circle cx="245" cy="745" r="20" fill="var(--wine-bright)"/>
    <text class="brand" x="245" y="792" font-size="22" fill="var(--cream-light)" text-anchor="middle">MAISON TAUREL</text>
    <text class="brand" x="245" y="815" font-size="7" fill="var(--wine-bright)" text-anchor="middle" letter-spacing="2">SINCE · DEPUIS 1938</text>
  </svg>
</main>
</body>
</html>
```